Heart Rate Game Display Graphic

We need a unique layout / info-graphic for our heart rate software to display an individuals hear rate, HR%, and other data together within a larger class of up to 40 other users. Graphics should be colorful, dynamic, and intuitive.

Target Market(s)

Group Fitness Classes

Font styles to use
Sans Serif

Colors

Designer to choose colors to be used in the design.

Requirements
Must have
• Individual Box must contain data field or graphic representation of:
• User Name
• Heart Rate %
• Points Earned / % Accuracy
Nice to have
• thinking other shape design that easily integrates with 40+ of the same shape. Looking for depth of design and or some 3d visualizations. Competing companies:
• https://www.pulsekite.org/
• https://www.gorvo.com/
• https://www.trevank.com/us-en/club
• https://vumbralo.com/
• https://kelvaro.fit/personal-trainer/
• https://www.dashoply.io/Solutions/Heart-Rate-Training
• http://nuvo.bramfieldsystems.com/
• https://lomi-wheel.com/explore/lomi-wheel-indoor-cycling-app/
Should not have
• should NOT be just be plain squares representing each client.

```html
<!DOCTYPE html>
<html lang="en">
<head>
<meta charset="utf-8">
<title>Heart Rate Game Display Graphic</title>
<link rel="stylesheet" href="https://fonts.googleapis.com/css2?family=Montserrat:wght@700;800;900&family=Syncopate:wght@700&display=swap">
<style>
  :root {
    --frame: #131420;
    --amber: #eba021;
    --amber-deep: #d58a17;
    --amber-light: #f3ad2c;
    --title-orange: #e1650a;
    --title-yellow: #f2a61f;
    --tile-dark: #161728;
    --tile-navy: #14213f;
    --card-ink: #151624;
    --badge-red: #e0262b;
    --portrait-a: #b9b6b3;
    --portrait-b: #e6e4e2;
    --white: #ffffff;
  }
  * { box-sizing: border-box; margin: 0; padding: 0; }
  html, body { width: 1200px; height: 823px; overflow: hidden; background: var(--frame); }
  .canvas {
    position: relative; width: 1200px; height: 823px; overflow: hidden;
    background: var(--frame);
    font-family: "Montserrat", Arial, sans-serif;
  }
  .backdrop {
    position: absolute; left: 9px; top: 9px; width: 1182px; height: 781px;
    background: linear-gradient(135deg, var(--amber-light) 0%, var(--amber) 45%, var(--amber-deep) 100%);
  }
  .title-bar { position: absolute; left: 60px; top: 52px; height: 57px; width: 1071px; display: flex; }
  .title-bar__cap-left { width: 42px; background: var(--title-orange); }
  .title-bar__cap-right { width: 41px; background: var(--title-yellow); }
  .title-bar__body { flex: 1; background: var(--frame); display: flex; align-items: center; justify-content: center; }
  .title-bar__text {
    font-family: "Syncopate", "Arial Black", sans-serif; font-weight: 700;
    font-size: 28px; letter-spacing: 2px; color: var(--white); white-space: nowrap;
  }
  .footer {
    position: absolute; left: 0; bottom: 0; width: 1200px; height: 33px;
    display: flex; align-items: center; justify-content: space-between; padding: 0 26px;
    font-family: "Syncopate", "Arial Black", sans-serif; font-weight: 700; color: var(--white);
  }
  .footer__title, .footer__year { font-size: 15px; letter-spacing: 1px; }

  .column { position: absolute; width: 140px; }
  .column--odd { top: 193px; }
  .column--even { top: 132px; }
  .tile { position: relative; width: 140px; height: 121px; }
  .tile-shape { position: absolute; left: 0; top: 0; width: 140px; height: 121px; overflow: visible; }
  .column--odd .tile-shape { fill: var(--tile-dark); }
  .column--even .tile-shape { fill: var(--tile-navy); }

  .card { position: absolute; left: 17px; top: 15px; width: 118px; height: 92px; color: var(--card-ink); }
  .card > span { position: absolute; white-space: nowrap; line-height: 1; }
  .card-photo {
    position: absolute; left: 0; top: 0; width: 118px; height: 92px;
    background: linear-gradient(160deg, var(--portrait-a), var(--portrait-b));
    clip-path: polygon(5px 46px, 25px 6px, 40px 6px, 34px 24px, 40px 38px, 40px 54px, 33px 70px, 38px 86px, 25px 86px);
  }
  .card-badge { left: 31px; top: 5px; width: 8px; height: 8px; border-radius: 50%; background: var(--badge-red); }
  .card-rate { left: 39px; top: 16px; font-size: 15px; font-weight: 800; }
  .card-rank { left: 89px; top: 24px; font-size: 8px; font-weight: 800; }
  .card-name { left: 47px; top: 43px; font-size: 6px; font-weight: 800; color: var(--white); }
  .card-points { left: 38px; top: 59px; font-size: 8px; font-weight: 800; }
  .card-accuracy { left: 65px; top: 59px; font-size: 8px; font-weight: 800; }
  .card-points-label { left: 29px; top: 72px; font-size: 3.6px; font-weight: 700; color: var(--white); letter-spacing: .6px; text-align: center; line-height: 1.2 !important; }
  .card-pct { left: 63px; top: 69px; font-size: 9px; font-weight: 800; color: var(--white); }
  .card-accuracy-label { left: 57px; top: 79px; font-size: 3.6px; font-weight: 700; color: var(--white); letter-spacing: .4px; }
</style>
</head>
<body>
<div class="canvas">
  <svg width="0" height="0" style="position:absolute" aria-hidden="true">
    <defs>
      <symbol id="tile-art" viewBox="0 0 140 121">
        <polygon points="0,60.5 35,0 105,0 140,60.5 105,121 35,121"/>
        <g transform="translate(17 15)">
          <polygon points="1,46 23,2 92,2 110,36 117,36 117,52 110,56 92,90 23,90" fill="#6cc644" stroke="#2e9b3a" stroke-width="1.2"/>
          <polygon points="4,46 24.5,4.5 90.5,4.5 108,37 108,55 90.5,87.5 24.5,87.5" fill="#3fae3a"/>
          <polygon points="26,6 90,6 107,38 10,38" fill="#f1f1f3"/>
          <polygon points="10,54 106,54 89,86 26,86" fill="#f7931e"/>
          <polygon points="63,54 106,54 89,86 48,86" fill="#f6ae1d"/>
          <polygon points="40,38 112,38 115,46 112,54 40,54" fill="#151624"/>
        </g>
      </symbol>
    </defs>
  </svg>

  <div class="backdrop" role="img" aria-label="Warm amber honeycomb backdrop"></div>

  <header class="title-bar">
    <div class="title-bar__cap-left"></div>
    <div class="title-bar__body"><h1 class="title-bar__text">HEART RATE GAME DISPLAY GRAPHIC</h1></div>
    <div class="title-bar__cap-right"></div>
  </header>

  <main class="board">
    <div class="column column--odd" style="left:110px">
      <div class="tile"><svg class="tile-shape" viewBox="0 0 140 121"><use href="#tile-art"/></svg><div class="card"><div class="card-photo" role="img" aria-label="Member portrait photo"></div><span class="card-badge"></span><span class="card-rate">100%</span><span class="card-rank">#1</span><span class="card-name">MARLOW KESTREL</span><span class="card-points">1200</span><span class="card-accuracy">60%</span><span class="card-points-label">POINTS<br>EARNED</span><span class="card-pct">%</span><span class="card-accuracy-label">ACCURACY</span></div></div>
      <div class="tile"><svg class="tile-shape" viewBox="0 0 140 121"><use href="#tile-art"/></svg><div class="card"><div class="card-photo" role="img" aria-label="Member portrait photo"></div><span class="card-badge"></span><span class="card-rate">100%</span><span class="card-rank">#1</span><span class="card-name">MARLOW KESTREL</span><span class="card-points">1200</span><span class="card-accuracy">60%</span><span class="card-points-label">POINTS<br>EARNED</span><span class="card-pct">%</span><span class="card-accuracy-label">ACCURACY</span></div></div>
      <div class="tile"><svg class="tile-shape" viewBox="0 0 140 121"><use href="#tile-art"/></svg><div class="card"><div class="card-photo" role="img" aria-label="Member portrait photo"></div><span class="card-badge"></span><span class="card-rate">100%</span><span class="card-rank">#1</span><span class="card-name">MARLOW KESTREL</span><span class="card-points">1200</span><span class="card-accuracy">60%</span><span class="card-points-label">POINTS<br>EARNED</span><span class="card-pct">%</span><span class="card-accuracy-label">ACCURACY</span></div></div>
      <div class="tile"><svg class="tile-shape" viewBox="0 0 140 121"><use href="#tile-art"/></svg><div class="card"><div class="card-photo" role="img" aria-label="Member portrait photo"></div><span class="card-badge"></span><span class="card-rate">100%</span><span class="card-rank">#1</span><span class="card-name">MARLOW KESTREL</span><span class="card-points">1200</span><span class="card-accuracy">60%</span><span class="card-points-label">POINTS<br>EARNED</span><span class="card-pct">%</span><span class="card-accuracy-label">ACCURACY</span></div></div>
    </div>

    <div class="column column--even" style="left:215px">
      <div class="tile"><svg class="tile-shape" viewBox="0 0 140 121"><use href="#tile-art"/></svg><div class="card"><div class="card-photo" role="img" aria-label="Member portrait photo"></div><span class="card-badge"></span><span class="card-rate">100%</span><span class="card-rank">#1</span><span class="card-name">MARLOW KESTREL</span><span class="card-points">1200</span><span class="card-accuracy">60%</span><span class="card-points-label">POINTS<br>EARNED</span><span class="card-pct">%</span><span class="card-accuracy-label">ACCURACY</span></div></div>
      <div class="tile"><svg class="tile-shape" viewBox="0 0 140 121"><use href="#tile-art"/></svg><div class="card"><div class="card-photo" role="img" aria-label="Member portrait photo"></div><span class="card-badge"></span><span class="card-rate">100%</span><span class="card-rank">#1</span><span class="card-name">MARLOW KESTREL</span><span class="card-points">1200</span><span class="card-accuracy">60%</span><span class="card-points-label">POINTS<br>EARNED</span><span class="card-pct">%</span><span class="card-accuracy-label">ACCURACY</span></div></div>
      <div class="tile"><svg class="tile-shape" viewBox="0 0 140 121"><use href="#tile-art"/></svg><div class="card"><div class="card-photo" role="img" aria-label="Member portrait photo"></div><span class="card-badge"></span><span class="card-rate">100%</span><span class="card-rank">#1</span><span class="card-name">MARLOW KESTREL</span><span class="card-points">1200</span><span class="card-accuracy">60%</span><span class="card-points-label">POINTS<br>EARNED</span><span class="card-pct">%</span><span class="card-accuracy-label">ACCURACY</span></div></div>
      <div class="tile"><svg class="tile-shape" viewBox="0 0 140 121"><use href="#tile-art"/></svg><div class="card"><div class="card-photo" role="img" aria-label="Member portrait photo"></div><span class="card-badge"></span><span class="card-rate">100%</span><span class="card-rank">#1</span><span class="card-name">MARLOW KESTREL</span><span class="card-points">1200</span><span class="card-accuracy">60%</span><span class="card-points-label">POINTS<br>EARNED</span><span class="card-pct">%</span><span class="card-accuracy-label">ACCURACY</span></div></div>
      <div class="tile"><svg class="tile-shape" viewBox="0 0 140 121"><use href="#tile-art"/></svg><div class="card"><div class="card-photo" role="img" aria-label="Member portrait photo"></div><span class="card-badge"></span><span class="card-rate">100%</span><span class="card-rank">#1</span><span class="card-name">MARLOW KESTREL</span><span class="card-points">1200</span><span class="card-accuracy">60%</span><span class="card-points-label">POINTS<br>EARNED</span><span class="card-pct">%</span><span class="card-accuracy-label">ACCURACY</span></div></div>
    </div>

    <div class="column column--odd" style="left:320px">
      <div class="tile"><svg class="tile-shape" viewBox="0 0 140 121"><use href="#tile-art"/></svg><div class="card"><div class="card-photo" role="img" aria-label="Member portrait photo"></div><span class="card-badge"></span><span class="card-rate">100%</span><span class="card-rank">#1</span><span class="card-name">MARLOW KESTREL</span><span class="card-points">1200</span><span class="card-accuracy">60%</span><span class="card-points-label">POINTS<br>EARNED</span><span class="card-pct">%</span><span class="card-accuracy-label">ACCURACY</span></div></div>
      <div class="tile"><svg class="tile-shape" viewBox="0 0 140 121"><use href="#tile-art"/></svg><div class="card"><div class="card-photo" role="img" aria-label="Member portrait photo"></div><span class="card-badge"></span><span class="card-rate">100%</span><span class="card-rank">#1</span><span class="card-name">MARLOW KESTREL</span><span class="card-points">1200</span><span class="card-accuracy">60%</span><span class="card-points-label">POINTS<br>EARNED</span><span class="card-pct">%</span><span class="card-accuracy-label">ACCURACY</span></div></div>
      <div class="tile"><svg class="tile-shape" viewBox="0 0 140 121"><use href="#tile-art"/></svg><div class="card"><div class="card-photo" role="img" aria-label="Member portrait photo"></div><span class="card-badge"></span><span class="card-rate">100%</span><span class="card-rank">#1</span><span class="card-name">MARLOW KESTREL</span><span class="card-points">1200</span><span class="card-accuracy">60%</span><span class="card-points-label">POINTS<br>EARNED</span><span class="card-pct">%</span><span class="card-accuracy-label">ACCURACY</span></div></div>
      <div class="tile"><svg class="tile-shape" viewBox="0 0 140 121"><use href="#tile-art"/></svg><div class="card"><div class="card-photo" role="img" aria-label="Member portrait photo"></div><span class="card-badge"></span><span class="card-rate">100%</span><span class="card-rank">#1</span><span class="card-name">MARLOW KESTREL</span><span class="card-points">1200</span><span class="card-accuracy">60%</span><span class="card-points-label">POINTS<br>EARNED</span><span class="card-pct">%</span><span class="card-accuracy-label">ACCURACY</span></div></div>
    </div>

    <div class="column column--even" style="left:425px">
      <div class="tile"><svg class="tile-shape" viewBox="0 0 140 121"><use href="#tile-art"/></svg><div class="card"><div class="card-photo" role="img" aria-label="Member portrait photo"></div><span class="card-badge"></span><span class="card-rate">100%</span><span class="card-rank">#1</span><span class="card-name">MARLOW KESTREL</span><span class="card-points">1200</span><span class="card-accuracy">60%</span><span class="card-points-label">POINTS<br>EARNED</span><span class="card-pct">%</span><span class="card-accuracy-label">ACCURACY</span></div></div>
      <div class="tile"><svg class="tile-shape" viewBox="0 0 140 121"><use href="#tile-art"/></svg><div class="card"><div class="card-photo" role="img" aria-label="Member portrait photo"></div><span class="card-badge"></span><span class="card-rate">100%</span><span class="card-rank">#1</span><span class="card-name">MARLOW KESTREL</span><span class="card-points">1200</span><span class="card-accuracy">60%</span><span class="card-points-label">POINTS<br>EARNED</span><span class="card-pct">%</span><span class="card-accuracy-label">ACCURACY</span></div></div>
      <div class="tile"><svg class="tile-shape" viewBox="0 0 140 121"><use href="#tile-art"/></svg><div class="card"><div class="card-photo" role="img" aria-label="Member portrait photo"></div><span class="card-badge"></span><span class="card-rate">100%</span><span class="card-rank">#1</span><span class="card-name">MARLOW KESTREL</span><span class="card-points">1200</span><span class="card-accuracy">60%</span><span class="card-points-label">POINTS<br>EARNED</span><span class="card-pct">%</span><span class="card-accuracy-label">ACCURACY</span></div></div>
      <div class="tile"><svg class="tile-shape" viewBox="0 0 140 121"><use href="#tile-art"/></svg><div class="card"><div class="card-photo" role="img" aria-label="Member portrait photo"></div><span class="card-badge"></span><span class="card-rate">100%</span><span class="card-rank">#1</span><span class="card-name">MARLOW KESTREL</span><span class="card-points">1200</span><span class="card-accuracy">60%</span><span class="card-points-label">POINTS<br>EARNED</span><span class="card-pct">%</span><span class="card-accuracy-label">ACCURACY</span></div></div>
      <div class="tile"><svg class="tile-shape" viewBox="0 0 140 121"><use href="#tile-art"/></svg><div class="card"><div class="card-photo" role="img" aria-label="Member portrait photo"></div><span class="card-badge"></span><span class="card-rate">100%</span><span class="card-rank">#1</span><span class="card-name">MARLOW KESTREL</span><span class="card-points">1200</span><span class="card-accuracy">60%</span><span class="card-points-label">POINTS<br>EARNED</span><span class="card-pct">%</span><span class="card-accuracy-label">ACCURACY</span></div></div>
    </div>

    <div class="column column--odd" style="left:530px">
      <div class="tile"><svg class="tile-shape" viewBox="0 0 140 121"><use href="#tile-art"/></svg><div class="card"><div class="card-photo" role="img" aria-label="Member portrait photo"></div><span class="card-badge"></span><span class="card-rate">100%</span><span class="card-rank">#1</span><span class="card-name">MARLOW KESTREL</span><span class="card-points">1200</span><span class="card-accuracy">60%</span><span class="card-points-label">POINTS<br>EARNED</span><span class="card-pct">%</span><span class="card-accuracy-label">ACCURACY</span></div></div>
      <div class="tile"><svg class="tile-shape" viewBox="0 0 140 121"><use href="#tile-art"/></svg><div class="card"><div class="card-photo" role="img" aria-label="Member portrait photo"></div><span class="card-badge"></span><span class="card-rate">100%</span><span class="card-rank">#1</span><span class="card-name">MARLOW KESTREL</span><span class="card-points">1200</span><span class="card-accuracy">60%</span><span class="card-points-label">POINTS<br>EARNED</span><span class="card-pct">%</span><span class="card-accuracy-label">ACCURACY</span></div></div>
      <div class="tile"><svg class="tile-shape" viewBox="0 0 140 121"><use href="#tile-art"/></svg><div class="card"><div class="card-photo" role="img" aria-label="Member portrait photo"></div><span class="card-badge"></span><span class="card-rate">100%</span><span class="card-rank">#1</span><span class="card-name">MARLOW KESTREL</span><span class="card-points">1200</span><span class="card-accuracy">60%</span><span class="card-points-label">POINTS<br>EARNED</span><span class="card-pct">%</span><span class="card-accuracy-label">ACCURACY</span></div></div>
      <div class="tile"><svg class="tile-shape" viewBox="0 0 140 121"><use href="#tile-art"/></svg><div class="card"><div class="card-photo" role="img" aria-label="Member portrait photo"></div><span class="card-badge"></span><span class="card-rate">100%</span><span class="card-rank">#1</span><span class="card-name">MARLOW KESTREL</span><span class="card-points">1200</span><span class="card-accuracy">60%</span><span class="card-points-label">POINTS<br>EARNED</span><span class="card-pct">%</span><span class="card-accuracy-label">ACCURACY</span></div></div>
    </div>

    <div class="column column--even" style="left:635px">
      <div class="tile"><svg class="tile-shape" viewBox="0 0 140 121"><use href="#tile-art"/></svg><div class="card"><div class="card-photo" role="img" aria-label="Member portrait photo"></div><span class="card-badge"></span><span class="card-rate">100%</span><span class="card-rank">#1</span><span class="card-name">MARLOW KESTREL</span><span class="card-points">1200</span><span class="card-accuracy">60%</span><span class="card-points-label">POINTS<br>EARNED</span><span class="card-pct">%</span><span class="card-accuracy-label">ACCURACY</span></div></div>
      <div class="tile"><svg class="tile-shape" viewBox="0 0 140 121"><use href="#tile-art"/></svg><div class="card"><div class="card-photo" role="img" aria-label="Member portrait photo"></div><span class="card-badge"></span><span class="card-rate">100%</span><span class="card-rank">#1</span><span class="card-name">MARLOW KESTREL</span><span class="card-points">1200</span><span class="card-accuracy">60%</span><span class="card-points-label">POINTS<br>EARNED</span><span class="card-pct">%</span><span class="card-accuracy-label">ACCURACY</span></div></div>
      <div class="tile"><svg class="tile-shape" viewBox="0 0 140 121"><use href="#tile-art"/></svg><div class="card"><div class="card-photo" role="img" aria-label="Member portrait photo"></div><span class="card-badge"></span><span class="card-rate">100%</span><span class="card-rank">#1</span><span class="card-name">MARLOW KESTREL</span><span class="card-points">1200</span><span class="card-accuracy">60%</span><span class="card-points-label">POINTS<br>EARNED</span><span class="card-pct">%</span><span class="card-accuracy-label">ACCURACY</span></div></div>
      <div class="tile"><svg class="tile-shape" viewBox="0 0 140 121"><use href="#tile-art"/></svg><div class="card"><div class="card-photo" role="img" aria-label="Member portrait photo"></div><span class="card-badge"></span><span class="card-rate">100%</span><span class="card-rank">#1</span><span class="card-name">MARLOW KESTREL</span><span class="card-points">1200</span><span class="card-accuracy">60%</span><span class="card-points-label">POINTS<br>EARNED</span><span class="card-pct">%</span><span class="card-accuracy-label">ACCURACY</span></div></div>
      <div class="tile"><svg class="tile-shape" viewBox="0 0 140 121"><use href="#tile-art"/></svg><div class="card"><div class="card-photo" role="img" aria-label="Member portrait photo"></div><span class="card-badge"></span><span class="card-rate">100%</span><span class="card-rank">#1</span><span class="card-name">MARLOW KESTREL</span><span class="card-points">1200</span><span class="card-accuracy">60%</span><span class="card-points-label">POINTS<br>EARNED</span><span class="card-pct">%</span><span class="card-accuracy-label">ACCURACY</span></div></div>
    </div>

    <div class="column column--odd" style="left:740px">
      <div class="tile"><svg class="tile-shape" viewBox="0 0 140 121"><use href="#tile-art"/></svg><div class="card"><div class="card-photo" role="img" aria-label="Member portrait photo"></div><span class="card-badge"></span><span class="card-rate">100%</span><span class="card-rank">#1</span><span class="card-name">MARLOW KESTREL</span><span class="card-points">1200</span><span class="card-accuracy">60%</span><span class="card-points-label">POINTS<br>EARNED</span><span class="card-pct">%</span><span class="card-accuracy-label">ACCURACY</span></div></div>
      <div class="tile"><svg class="tile-shape" viewBox="0 0 140 121"><use href="#tile-art"/></svg><div class="card"><div class="card-photo" role="img" aria-label="Member portrait photo"></div><span class="card-badge"></span><span class="card-rate">100%</span><span class="card-rank">#1</span><span class="card-name">MARLOW KESTREL</span><span class="card-points">1200</span><span class="card-accuracy">60%</span><span class="card-points-label">POINTS<br>EARNED</span><span class="card-pct">%</span><span class="card-accuracy-label">ACCURACY</span></div></div>
      <div class="tile"><svg class="tile-shape" viewBox="0 0 140 121"><use href="#tile-art"/></svg><div class="card"><div class="card-photo" role="img" aria-label="Member portrait photo"></div><span class="card-badge"></span><span class="card-rate">100%</span><span class="card-rank">#1</span><span class="card-name">MARLOW KESTREL</span><span class="card-points">1200</span><span class="card-accuracy">60%</span><span class="card-points-label">POINTS<br>EARNED</span><span class="card-pct">%</span><span class="card-accuracy-label">ACCURACY</span></div></div>
      <div class="tile"><svg class="tile-shape" viewBox="0 0 140 121"><use href="#tile-art"/></svg><div class="card"><div class="card-photo" role="img" aria-label="Member portrait photo"></div><span class="card-badge"></span><span class="card-rate">100%</span><span class="card-rank">#1</span><span class="card-name">MARLOW KESTREL</span><span class="card-points">1200</span><span class="card-accuracy">60%</span><span class="card-points-label">POINTS<br>EARNED</span><span class="card-pct">%</span><span class="card-accuracy-label">ACCURACY</span></div></div>
    </div>

    <div class="column column--even" style="left:845px">
      <div class="tile"><svg class="tile-shape" viewBox="0 0 140 121"><use href="#tile-art"/></svg><div class="card"><div class="card-photo" role="img" aria-label="Member portrait photo"></div><span class="card-badge"></span><span class="card-rate">100%</span><span class="card-rank">#1</span><span class="card-name">MARLOW KESTREL</span><span class="card-points">1200</span><span class="card-accuracy">60%</span><span class="card-points-label">POINTS<br>EARNED</span><span class="card-pct">%</span><span class="card-accuracy-label">ACCURACY</span></div></div>
      <div class="tile"><svg class="tile-shape" viewBox="0 0 140 121"><use href="#tile-art"/></svg><div class="card"><div class="card-photo" role="img" aria-label="Member portrait photo"></div><span class="card-badge"></span><span class="card-rate">100%</span><span class="card-rank">#1</span><span class="card-name">MARLOW KESTREL</span><span class="card-points">1200</span><span class="card-accuracy">60%</span><span class="card-points-label">POINTS<br>EARNED</span><span class="card-pct">%</span><span class="card-accuracy-label">ACCURACY</span></div></div>
      <div class="tile"><svg class="tile-shape" viewBox="0 0 140 121"><use href="#tile-art"/></svg><div class="card"><div class="card-photo" role="img" aria-label="Member portrait photo"></div><span class="card-badge"></span><span class="card-rate">100%</span><span class="card-rank">#1</span><span class="card-name">MARLOW KESTREL</span><span class="card-points">1200</span><span class="card-accuracy">60%</span><span class="card-points-label">POINTS<br>EARNED</span><span class="card-pct">%</span><span class="card-accuracy-label">ACCURACY</span></div></div>
      <div class="tile"><svg class="tile-shape" viewBox="0 0 140 121"><use href="#tile-art"/></svg><div class="card"><div class="card-photo" role="img" aria-label="Member portrait photo"></div><span class="card-badge"></span><span class="card-rate">100%</span><span class="card-rank">#1</span><span class="card-name">MARLOW KESTREL</span><span class="card-points">1200</span><span class="card-accuracy">60%</span><span class="card-points-label">POINTS<br>EARNED</span><span class="card-pct">%</span><span class="card-accuracy-label">ACCURACY</span></div></div>
      <div class="tile"><svg class="tile-shape" viewBox="0 0 140 121"><use href="#tile-art"/></svg><div class="card"><div class="card-photo" role="img" aria-label="Member portrait photo"></div><span class="card-badge"></span><span class="card-rate">100%</span><span class="card-rank">#1</span><span class="card-name">MARLOW KESTREL</span><span class="card-points">1200</span><span class="card-accuracy">60%</span><span class="card-points-label">POINTS<br>EARNED</span><span class="card-pct">%</span><span class="card-accuracy-label">ACCURACY</span></div></div>
    </div>

    <div class="column column--odd" style="left:950px">
      <div class="tile"><svg class="tile-shape" viewBox="0 0 140 121"><use href="#tile-art"/></svg><div class="card"><div class="card-photo" role="img" aria-label="Member portrait photo"></div><span class="card-badge"></span><span class="card-rate">100%</span><span class="card-rank">#1</span><span class="card-name">MARLOW KESTREL</span><span class="card-points">1200</span><span class="card-accuracy">60%</span><span class="card-points-label">POINTS<br>EARNED</span><span class="card-pct">%</span><span class="card-accuracy-label">ACCURACY</span></div></div>
      <div class="tile"><svg class="tile-shape" viewBox="0 0 140 121"><use href="#tile-art"/></svg><div class="card"><div class="card-photo" role="img" aria-label="Member portrait photo"></div><span class="card-badge"></span><span class="card-rate">100%</span><span class="card-rank">#1</span><span class="card-name">MARLOW KESTREL</span><span class="card-points">1200</span><span class="card-accuracy">60%</span><span class="card-points-label">POINTS<br>EARNED</span><span class="card-pct">%</span><span class="card-accuracy-label">ACCURACY</span></div></div>
      <div class="tile"><svg class="tile-shape" viewBox="0 0 140 121"><use href="#tile-art"/></svg><div class="card"><div class="card-photo" role="img" aria-label="Member portrait photo"></div><span class="card-badge"></span><span class="card-rate">100%</span><span class="card-rank">#1</span><span class="card-name">MARLOW KESTREL</span><span class="card-points">1200</span><span class="card-accuracy">60%</span><span class="card-points-label">POINTS<br>EARNED</span><span class="card-pct">%</span><span class="card-accuracy-label">ACCURACY</span></div></div>
      <div class="tile"><svg class="tile-shape" viewBox="0 0 140 121"><use href="#tile-art"/></svg><div class="card"><div class="card-photo" role="img" aria-label="Member portrait photo"></div><span class="card-badge"></span><span class="card-rate">100%</span><span class="card-rank">#1</span><span class="card-name">MARLOW KESTREL</span><span class="card-points">1200</span><span class="card-accuracy">60%</span><span class="card-points-label">POINTS<br>EARNED</span><span class="card-pct">%</span><span class="card-accuracy-label">ACCURACY</span></div></div>
    </div>
  </main>

  <footer class="footer">
    <span class="footer__title">HEART RATE GAME DISPLAY GRAPHIC</span>
    <span class="footer__year">2020</span>
  </footer>
</div>
</body>
</html>
```